A Real Estate Company Needs a Business Card Design

We need a business card design for a new company based in Boston MA called "Brackenfield Real Estate LLC" we are a small company but we like a big corporate look, a simple, sleek, modern and progressive look. we would like the option of having a design that could include the real estate agents personal photo and also a design if the realtor decides not to have a photo. we do not have LOGO at this moment, please use any property look pic corporate with word" Brackenfield Real Estate LLC" please see attached file as an example.
Industry/Entity Type
Business

```html
<!DOCTYPE html>
<html lang="en">
<head>
<meta charset="utf-8">
<title>Brackenfield Real Estate LLC — Business Cards</title>
<link href="https://fonts.googleapis.com/css2?family=Open+Sans:wght@400;600&display=swap" rel="stylesheet">
<style>
  :root {
    --brown: #4a2410;
    --brown-card: #5a3218;
    --white: #ffffff;
    --paper: #e9e7e4;
    --ink: #3a2a20;
    --photo: #231f20;
    --rule: #b9aca3;
  }
  * { margin: 0; padding: 0; box-sizing: border-box; }
  html, body { width: 1200px; height: 1000px; overflow: hidden; }
  body {
    background: var(--paper);
    font-family: "Open Sans", Arial, sans-serif;
    color: var(--ink);
    position: relative;
  }
  .brand-band {
    position: absolute; left: 0; top: 0; width: 1200px; height: 125px;
    background: var(--brown);
    display: flex; align-items: center; justify-content: center;
  }
  .wordmark {
    display: flex; align-items: center; gap: 10px;
    font-weight: 400; letter-spacing: 3px; text-transform: uppercase;
    line-height: 1.3; text-align: center;
  }
  .wordmark .mark-square { width: 10px; height: 10px; background: currentColor; flex: none; }
  .brand-band .wordmark { color: var(--white); font-size: 17px; }

  .card {
    position: absolute; top: 250px; width: 330px; height: 560px;
    box-shadow: 0 10px 24px rgba(0,0,0,.18);
    overflow: hidden;
  }
  .card-front { left: 220px; background: var(--white); }
  .card-back {
    left: 650px; background: var(--brown-card); color: var(--white);
    display: flex; flex-direction: column; align-items: center; justify-content: center;
  }

  .stripes { position: absolute; display: flex; gap: 7px; }
  .stripes span { display: block; width: 6px; background: var(--brown); }
  .stripes-left { left: 18px; top: 0; align-items: flex-start; }
  .stripes-left span:nth-child(1) { height: 260px; }
  .stripes-left span:nth-child(2) { height: 230px; }
  .stripes-left span:nth-child(3) { height: 200px; }
  .stripes-right { right: 18px; bottom: 0; align-items: flex-end; }
  .stripes-right span:nth-child(1) { height: 150px; }
  .stripes-right span:nth-child(2) { height: 180px; }
  .stripes-right span:nth-child(3) { height: 210px; }

  .front-info { position: absolute; left: 60px; top: 56px; width: 240px; }
  .card-front .wordmark { color: var(--brown); font-size: 13px; justify-content: flex-start; text-align: left; }
  .contact { margin-top: 30px; font-size: 12px; line-height: 1.8; }
  .divider { position: absolute; left: 60px; top: 260px; width: 200px; height: 1px; background: var(--rule); }
  .agent { position: absolute; left: 60px; top: 290px; width: 220px; }
  .agent-photo { width: 150px; height: 150px; background: var(--photo); }
  .agent-name { margin-top: 18px; font-size: 24px; font-weight: 600; color: var(--ink); line-height: 1.1; }
  .agent-title { font-size: 11px; letter-spacing: 1px; margin-top: 6px; }

  .card-back .wordmark { color: var(--white); font-size: 17px; }
  .web { margin-top: 24px; font-size: 13px; letter-spacing: .5px; }
</style>
</head>
<body>
  <header class="brand-band">
    <div class="wordmark"><span class="mark-square"></span><span>Brackenfield<br>Real Estate LLC</span></div>
  </header>

  <section class="card card-front">
    <div class="stripes stripes-left"><span></span><span></span><span></span></div>
    <div class="stripes stripes-right"><span></span><span></span><span></span></div>
    <div class="front-info">
      <div class="wordmark"><span class="mark-square"></span><span>Brackenfield<br>Real Estate LLC</span></div>
      <div class="contact">
        <p>P. (XXX) 123 1234</p>
        <p>A. Location</p>
        <p>E. name@domain.com</p>
      </div>
    </div>
    <div class="divider"></div>
    <div class="agent">
      <div class="agent-photo" role="img" aria-label="Agent portrait photo"></div>
      <p class="agent-name">YourName</p>
      <p class="agent-title">TITLE</p>
    </div>
  </section>

  <section class="card card-back">
    <div class="wordmark"><span class="mark-square"></span><span>Brackenfield<br>Real Estate LLC</span></div>
    <p class="web">www.yourdomain.com</p>
  </section>
</body>
</html>
```